IT Company need facebook graphics

We need a facebook logo and cover that matches more our website and other marketing materials which is quite uniform in colours.
We are a small company, we do not advertise much mainly word of mouth, but we want to try out some Facebook advertising and need our page to look amazing.
Something playful yet professional, something that will stand out in peoples mind.
Target Market(s)
Home users and small business
Industry/Entity Type
Computer Repair
Requirements
Must have
- A colour scheme to match existing website, but be playful and fun. Website is www.dovinaprix.com.au
Nice to have
- No input for nice to have, I trust the awesome talent out there to come up with something.
Should not have
- Again, no input for should not haves.

```html
<!DOCTYPE html>
<html lang="en">
<head>
<meta charset="utf-8">
<title>Dovina Prix – Facebook Cover</title>
<link href="https://fonts.googleapis.com/css2?family=Source+Sans+3:wght@400;700;900&display=swap" rel="stylesheet">
<style>
  :root {
    --orange: #f15a24;
    --brand-red: #e0201f;
    --charcoal: #323232;
    --panel-light: #ececec;
    --panel-mid: #dedede;
    --panel-low: #cfcfcf;
    --frame: #e4e4e4;
    --keys-dark: #2c2f34;
    --keys-mid: #6b6f76;
    --silver: #c6c9cd;
    --silver-light: #e2e3e5;
    --warm-light: #ddd6cc;
    --tube-orange: #e8643a;
    --white: #ffffff;
  }
  * { margin: 0; padding: 0; box-sizing: border-box; }
  html, body {
    width: 1200px; height: 444px; overflow: hidden;
    background: var(--white);
  }
  .cover {
    position: relative;
    width: 1200px; height: 444px;
    overflow: hidden;
    font-family: "Source Sans 3", "Helvetica Neue", Arial, sans-serif;
    background: var(--orange);
  }
  .cover__shapes {
    position: absolute; inset: 0;
    width: 1200px; height: 444px;
  }
  .brand {
    position: absolute;
    left: 24px; top: 24px;
    display: flex; align-items: center; gap: 10px;
  }
  .brand__dot {
    width: 24px; height: 24px; border-radius: 50%;
    background: var(--brand-red);
  }
  .brand__name {
    color: var(--brand-red);
    font-weight: 900;
    font-size: 42px;
    letter-spacing: -0.5px;
    line-height: 1;
    text-transform: uppercase;
  }
  .values {
    position: absolute;
    left: 270px; top: 118px;
    list-style: none;
    color: var(--white);
    font-size: 16px;
    line-height: 24px;
  }
  .values__item {
    display: flex; align-items: center; gap: 4px;
  }
  .values__tick {
    width: 9px; height: 9px; flex: none;
  }
  .contact {
    position: absolute;
    left: 89px; top: 224px;
    display: flex; align-items: center;
    color: var(--white);
    font-size: 16px;
    line-height: 22px;
  }
  .contact__item { display: flex; align-items: center; gap: 7px; }
  .contact__item + .contact__item { margin-left: 18px; }
  .contact__icon { width: 20px; height: 20px; flex: none; }
</style>
</head>
<body>
<main class="cover">
  <svg class="cover__shapes" viewBox="0 0 1200 444" xmlns="http://www.w3.org/2000/svg">
    <defs>
      <linearGradient id="laptopTone" x1="0" y1="0" x2="0.6" y2="1">
        <stop offset="0" stop-color="var(--panel-light)"/>
        <stop offset="0.45" stop-color="var(--panel-mid)"/>
        <stop offset="1" stop-color="var(--panel-low)"/>
      </linearGradient>
      <linearGradient id="deskTone" x1="0.05" y1="1" x2="0.95" y2="0">
        <stop offset="0" stop-color="var(--keys-dark)"/>
        <stop offset="0.3" stop-color="var(--keys-mid)"/>
        <stop offset="0.5" stop-color="var(--silver)"/>
        <stop offset="0.68" stop-color="var(--silver-light)"/>
        <stop offset="0.82" stop-color="#e3b9a6"/>
        <stop offset="1" stop-color="var(--warm-light)"/>
      </linearGradient>
    </defs>

    <!-- left pale panel -->
    <polygon points="13,0 578,0 454,444 13,444" fill="url(#laptopTone)"
             role="img" aria-label="Faded close-up of a laptop keyboard with a stethoscope"/>

    <!-- right photo panel with thin light frame -->
    <polygon points="727,0 1200,0 1076,444 600,444" fill="var(--frame)"/>
    <polygon points="733,0 1194,0 1070,444 606,444" fill="url(#deskTone)"
             role="img" aria-label="Laptop keyboard with an orange stethoscope lying across it"/>

    <!-- contact bar -->
    <polygon points="13,220 511,220 502,251 13,251" fill="var(--charcoal)"/>
    <!-- values box -->
    <polygon points="256,113 547,113 547,197 241,197" fill="var(--charcoal)"/>
  </svg>

  <div class="brand">
    <span class="brand__dot"></span>
    <span class="brand__name">Dovina Prix</span>
  </div>

  <ul class="values">
    <li class="values__item">
      <svg class="values__tick" viewBox="0 0 10 10"><rect width="10" height="10" rx="2" fill="var(--brand-red)"/><path d="M2.3 5.2l1.9 1.9 3.6-3.8" stroke="#fff" stroke-width="1.4" fill="none"/></svg>
      Professional Service
    </li>
    <li class="values__item">
      <svg class="values__tick" viewBox="0 0 10 10"><rect width="10" height="10" rx="2" fill="var(--brand-red)"/><path d="M2.3 5.2l1.9 1.9 3.6-3.8" stroke="#fff" stroke-width="1.4" fill="none"/></svg>
      Exceptional Quality
    </li>
    <li class="values__item">
      <svg class="values__tick" viewBox="0 0 10 10"><rect width="10" height="10" rx="2" fill="var(--brand-red)"/><path d="M2.3 5.2l1.9 1.9 3.6-3.8" stroke="#fff" stroke-width="1.4" fill="none"/></svg>
      Reliability
    </li>
  </ul>

  <div class="contact">
    <span class="contact__item">
      <svg class="contact__icon" viewBox="0 0 20 20"><circle cx="10" cy="10" r="8.8" fill="none" stroke="#fff" stroke-width="1.4"/><path d="M6.6 5.4l1.7-.3 1 2.4-1.1 1a6 6 0 0 0 3.3 3.3l1-1.1 2.4 1-.3 1.7c-4.6.4-8.4-3.4-8-8z" fill="#fff"/></svg>
      643-555-0178
    </span>
    <span class="contact__item">
      <svg class="contact__icon" viewBox="0 0 20 20" fill="none" stroke="#fff" stroke-width="1.3"><circle cx="10" cy="10" r="8.6"/><ellipse cx="10" cy="10" rx="3.8" ry="8.6"/><path d="M1.4 10h17.2M3 5.5h14M3 14.5h14"/></svg>
      www.dovinaprix.com.au
    </span>
  </div>
</main>
</body>
</html>
```